Business Card Design Project

The business card is for an educational company that provides personalised tuition to students.

The company logo is in orange and blue (as provided) and should be included in the name card design

The philosophy of the company is to make learning a comfortable experience for student as such design of the namecard should look fresh and has a bit of the 'wow' factor. Some of the namecard design that appeals to me are as uploaded under Sample Design.

The particulars that need to be provided are:
(1): Company Name (Quillmont Education)
(1): Name
(2): Educational qualifications which will appear below name
(3): Mobile number
(4): Email address
(5): Website

Industry/Entity Type

Business

Requirements
Must have
• (1): Company Logo

(2): The card background should preferably be coloured both for the front side and back.

(3): The choice of font is important as part of the selection consideration. There is no preferred font that I have selected, designer is free to choose the font that will complement their design.

```html
<!DOCTYPE html>
<html lang="en">
<head>
<meta charset="utf-8">
<title>Quillmont Education Business Cards</title>
<link rel="stylesheet" href="https://fonts.googleapis.com/css2?family=Libre+Baskerville:wght@400;700&family=Open+Sans:wght@400;600&display=swap">
<style>
  :root {
    --page-bg: #e9e9e9;
    --card-cream: #fbf8ef;
    --card-gold: #d9c99a;
    --card-gold-deep: #b9a46a;
    --ink: #1f1f1f;
    --ink-soft: #4a4a4a;
    --brand-grey: #5a5a5a;
    --brand-orange: #ef6a1f;
    --art-pink: #d9406e;
    --art-green: #7a9a3c;
    --art-gold: #c7ae62;
  }
  * { margin: 0; padding: 0; box-sizing: border-box; }
  html, body { width: 1200px; height: 861px; overflow: hidden; }
  body {
    background: var(--page-bg);
    position: relative;
    font-family: "Open Sans", Arial, sans-serif;
    color: var(--ink);
  }
  .card {
    position: absolute;
    top: 288px;
    width: 500px;
    height: 286px;
    border-radius: 14px;
    overflow: hidden;
    background:
      radial-gradient(ellipse at 55% 45%, var(--card-cream) 0%, rgba(251,248,239,0.6) 45%, rgba(217,201,154,0.5) 100%),
      linear-gradient(135deg, var(--card-gold) 0%, var(--card-cream) 50%, var(--card-gold) 100%);
    box-shadow: 0 6px 18px rgba(0,0,0,0.18);
  }
  .card--front { left: 70px; }
  .card--back { left: 630px; }

  .floral-art {
    position: absolute;
    border-radius: 40% 60% 55% 45%;
    background:
      radial-gradient(circle at 60% 40%, rgba(217,64,110,0.55) 0%, rgba(217,64,110,0) 35%),
      radial-gradient(circle at 30% 70%, rgba(122,154,60,0.45) 0%, rgba(122,154,60,0) 45%),
      radial-gradient(circle at 50% 50%, rgba(199,174,98,0.7) 0%, rgba(199,174,98,0) 70%);
  }
  .card--front .floral-art { left: 0; top: 10px; width: 250px; height: 260px; }
  .card--back .floral-art { right: 10px; top: 20px; width: 200px; height: 230px; }

  .brand {
    position: absolute;
    display: flex;
    align-items: center;
    gap: 10px;
  }
  .brand__mark {
    width: 44px;
    height: 44px;
    background: var(--brand-orange);
    border-radius: 4px;
    flex: none;
  }
  .brand__name {
    font-family: "Libre Baskerville", Georgia, serif;
    font-weight: 400;
    color: var(--brand-grey);
    font-size: 22px;
    line-height: 1.08;
  }
  .card--front .brand { left: 250px; top: 118px; }
  .card--back .brand { left: 36px; top: 48px; }
  .card--back .brand__mark { width: 62px; height: 62px; }
  .card--back .brand__name { font-size: 25px; }

  .front-url {
    position: absolute;
    left: 266px;
    top: 198px;
    font-size: 13px;
    color: var(--ink-soft);
  }

  .holder { position: absolute; left: 36px; top: 152px; }
  .holder__name {
    font-family: "Libre Baskerville", Georgia, serif;
    font-weight: 700;
    font-size: 24px;
    color: var(--ink);
  }
  .holder__role { font-size: 13px; color: var(--ink-soft); margin-top: 2px; }

  .contact {
    position: absolute;
    left: 36px;
    top: 222px;
    font-size: 12px;
    line-height: 17px;
    border-collapse: collapse;
  }
  .contact th { text-align: left; font-weight: 600; padding-right: 8px; }
  .contact td { color: var(--ink-soft); }
</style>
</head>
<body>
  <section class="card card--front" aria-label="Card front">
    <div class="floral-art" role="img" aria-label="Ornamental bird with floral paisley pattern in pink, green and gold"></div>
    <div class="brand">
      <span class="brand__mark"></span>
      <span class="brand__name">Quillmont<br>Education</span>
    </div>
    <p class="front-url">www.quillmonteducation.com</p>
  </section>

  <section class="card card--back" aria-label="Card back">
    <div class="floral-art" role="img" aria-label="Ornamental bird with floral paisley pattern in pink, green and gold"></div>
    <div class="brand">
      <span class="brand__mark"></span>
      <span class="brand__name">Quillmont<br>Education</span>
    </div>
    <div class="holder">
      <p class="holder__name">Name Surname</p>
      <p class="holder__role">Educational qualifications</p>
    </div>
    <table class="contact">
      <tr><th>Mobile</th><td>: 123.456.7890</td></tr>
      <tr><th>Email</th><td>: name@quillmonteducation.com</td></tr>
      <tr><th>Website</th><td>: www.quillmonteducation.com</td></tr>
    </table>
  </section>
</body>
</html>
```